Harvest Gathering event flyer

I would like a church event flyer designed. The event is called "HARVEST GATHERING 2018". I am looking for a professional, yet catchy design that uses our brand colors and logo creatively while communicating key information of the event effectively.

1. The logo is attached in two color formats. The designer has the choice to use them as he/she want.

2. The location of the event is: Lindqvist Community Center, 482 Tamsworth Street, Portland, ME 04102
3. Time and date of event. The designer can organize and format the date and time as he/she pleases.
December 28th, 29th @ 7:00PM
December 30th @ 10:00AM
4. The topic of the event is "Tongues of fire". The designer is free to use this phrase as he/she pleases to create a good composition.
5. Speaker: Prophet Marcus Obuya
6. Contact information: contact@cedarbrookfellowship.org - Telephone number: 207 555 0148

7. I would also like the following three words on the flyer. These words describe the focus of the event: FIRE, REVIVAL, PROPHETIC

```html
<!DOCTYPE html>
<html lang="en">
<head>
<meta charset="utf-8">
<title>Harvest Gathering 2018</title>
<link rel="stylesheet" href="https://fonts.googleapis.com/css2?family=Cinzel:wght@400;600;700&family=Montserrat:wght@400;700&family=Courgette&display=swap">
<style>
  :root {
    --ink: #0b0a09;
    --flame: #f39a21;
    --gold: #f6a623;
    --white: #ffffff;
    --sky-deep: #3a1a06;
    --sky-mid: #b9560f;
    --sky-glow: #ffd27a;
  }
  * { margin: 0; padding: 0; box-sizing: border-box; }
  html, body { width: 946px; height: 1200px; overflow: hidden; background: var(--ink); }
  .flyer {
    position: relative; width: 946px; height: 1200px; overflow: hidden;
    background: var(--ink); color: var(--white);
    font-family: 'Montserrat', sans-serif;
  }
  .hero-photo {
    position: absolute; left: 0; top: 0; width: 946px; height: 500px;
    background:
      radial-gradient(ellipse 260px 200px at 470px 120px, var(--sky-glow) 0%, rgba(255,190,90,0.6) 35%, transparent 75%),
      linear-gradient(180deg, var(--sky-deep) 0%, var(--sky-mid) 30%, #c8661a 55%, #5a2a08 78%, var(--ink) 100%);
  }
  .flame-shape { position: absolute; left: 0; top: 0; }
  .brand {
    position: absolute; left: 57px; top: 60px;
    display: flex; align-items: center; gap: 10px;
    font-family: 'Cinzel', serif; font-weight: 400; font-size: 50px;
    color: var(--white); letter-spacing: 1px;
  }
  .brand-dot { width: 16px; height: 16px; border-radius: 50%; background: var(--flame); }
  .title {
    position: absolute; left: 0; width: 946px; top: 498px;
    text-align: center; font-family: 'Cinzel', serif; font-weight: 700;
    line-height: 1; color: var(--white);
  }
  .title-line1 { display: block; font-size: 104px; }
  .title-line2 { display: block; font-size: 80px; margin-top: 18px; }
  .title-year {
    position: absolute; left: 0; width: 946px; top: 718px; text-align: center;
    font-family: 'Courgette', cursive; font-size: 98px; color: var(--gold); line-height: 1;
  }
  .focus-banner { position: absolute; left: 165px; top: 845px; }
  .focus-text {
    position: absolute; left: 165px; top: 845px; width: 594px; height: 52px;
    display: flex; align-items: center; justify-content: center;
    font-family: 'Cinzel', serif; font-weight: 600; font-size: 30px; letter-spacing: 1px;
  }
  .kneeling-scene {
    position: absolute; left: 700px; top: 760px; width: 180px; height: 260px;
    background: radial-gradient(ellipse at 50% 60%, rgba(120,120,120,0.35), transparent 70%);
  }
  .schedule {
    position: absolute; left: 48px; top: 930px;
    font-family: 'Cinzel', serif; font-weight: 400; font-size: 29px; line-height: 36px;
  }
  .schedule .time { color: var(--gold); }
  .address {
    position: absolute; left: 48px; top: 1014px;
    display: flex; gap: 12px; font-size: 21px; line-height: 30px;
  }
  .contact {
    position: absolute; left: 48px; top: 1090px;
    display: flex; align-items: center; gap: 8px; font-size: 18px; font-weight: 700;
    white-space: nowrap;
  }
  .contact .divider { margin: 0 2px; }
  .speaker-band {
    position: absolute; left: 0; top: 1143px; width: 600px; height: 44px;
    background: var(--flame); color: var(--ink);
    font-weight: 700; font-size: 25px; line-height: 44px; padding-left: 44px;
  }
  .speaker-photo {
    position: absolute; left: 650px; top: 1030px; width: 296px; height: 170px;
    background: linear-gradient(180deg, #3b3631 0%, #1f1d1b 55%, #121212 100%);
  }
</style>
</head>
<body>
<main class="flyer">
  <div class="hero-photo" role="img" aria-label="Sunset sky with three crosses on a hill and glowing embers"></div>

  <svg class="flame-shape" width="946" height="1200" viewBox="0 0 946 1200" aria-hidden="true">
    <path d="M890 450 C790 520 745 650 838 760 C905 845 700 960 596 1200 L946 1200 L946 860 C855 785 870 610 890 450 Z" fill="var(--flame)"/>
  </svg>

  <div class="brand"><span class="brand-dot"></span>KESTRA</div>

  <h1 class="title">
    <span class="title-line1">HARVEST</span>
    <span class="title-line2">GATHERING</span>
  </h1>
  <div class="title-year">2018</div>

  <svg class="focus-banner" width="594" height="52" viewBox="0 0 594 52" aria-hidden="true">
    <path d="M24 1 H570 L593 26 L570 51 H24 L1 26 Z" fill="none" stroke="var(--flame)" stroke-width="2"/>
  </svg>
  <div class="focus-text">FIRE, REVIVAL, PROPHETIC</div>

  <div class="kneeling-scene" role="img" aria-label="Silhouette of a person kneeling before a cross"></div>

  <div class="schedule">
    <div>DECEMBER 28TH, 29TH @ <span class="time">7:00PM</span></div>
    <div>DECEMBER 30TH @ <span class="time">10:00AM</span></div>
  </div>

  <div class="address">
    <svg width="20" height="26" viewBox="0 0 20 26" aria-hidden="true" style="margin-top:3px">
      <path d="M10 1 C5 1 1 5 1 10 C1 17 10 25 10 25 C10 25 19 17 19 10 C19 5 15 1 10 1 Z" fill="var(--flame)"/>
      <circle cx="10" cy="10" r="3.5" fill="var(--ink)"/>
    </svg>
    <div>Lindqvist Community Center, 482<br>Tamsworth Street, Portland, ME 04102</div>
  </div>

  <div class="contact">
    <svg width="19" height="19" viewBox="0 0 20 20" aria-hidden="true">
      <circle cx="10" cy="10" r="10" fill="var(--white)"/>
      <rect x="5" y="6.5" width="10" height="7" fill="none" stroke="var(--ink)" stroke-width="1.5"/>
      <path d="M5 7 L10 11 L15 7" fill="none" stroke="var(--ink)" stroke-width="1.5"/>
    </svg>
    <span>contact@cedarbrookfellowship.org</span>
    <span class="divider">|</span>
    <svg width="19" height="19" viewBox="0 0 20 20" aria-hidden="true">
      <circle cx="10" cy="10" r="10" fill="var(--white)"/>
      <path d="M7 5 L9 8 L8 9.5 C8.7 11 9.5 11.8 11 12.5 L12.5 11.5 L15 13.5 L14 15 C10 15 5.5 10.5 5.5 6.5 Z" fill="var(--ink)"/>
    </svg>
    <span>207 555 0148</span>
  </div>

  <div class="speaker-band">SPEAKER: PROPHET MARCUS OBUYA</div>
  <div class="speaker-photo" role="img" aria-label="Portrait of the speaker, Prophet Marcus Obuya, in a dark blazer"></div>
</main>
</body>
</html>
```